Web Page for marketing online agency

We are an online marketing agency that is acing the direct response model. We engage with our customers throughout different marketing techniques as research copy-writing, advertisements and content writing. We would need a website design that will have four main aspects: The Vision; stating who we are, The Mission; stating what we do, The Team And It's Values, and a Contact Form. For this design we would want a sharp, clean and smart approach, with illustrated elements or suggestive images. You can use the attached copy, the logo, the USP and the motto. Please integrate them as you see fit while keeping in mind the previous needs and copy. This website is going to be our connection with our possible partners, future colleagues and even our clients. You may submit a design for one page or integrate the 4 different aspects on separate web pages.
Target Market(s)
business partners, future employees, age range 25-60
Industry/Entity Type
Direct Marketing
Number of Pages Required
1 page
Requirements
Must have
- Menu / Header
- 4 Parts or 4 Pages including: vision, mission, team, contact
- Logo
- Motto: Direct Brilliance
- USP: We help people help themselves.
- The copy attached
Nice to have
- Representative illustrated images or elements
Should not have
- A boring design, classical design - Pagequill like

```html
<!DOCTYPE html>
<html lang="en">
<head>
<meta charset="utf-8">
<title>BrightKin — Direct Brilliance</title>
<link rel="stylesheet" href="https://fonts.googleapis.com/css2?family=Montserrat:wght@400;500;600;700&display=swap">
<style>
:root{
  --ink:#1f1f1f;
  --text:#333;
  --accent:#c9c31c;
  --blue:#2aa3dc;
  --mission:#8ec3da;
  --contact-top:#8cc6e0;
  --contact-bottom:#2a9fdc;
  --footer:#1393d6;
  --white:#fff;
  --field:#fff;
  --field-line:#d7dfe4;
}
*{box-sizing:border-box;margin:0;padding:0}
html,body{width:711px;height:1200px;overflow:hidden}
body{position:relative;font-family:"Montserrat",Arial,sans-serif;color:var(--text);background:var(--white);font-size:7px;line-height:1.5}
.abs{position:absolute}

/* header */
.site-header{position:absolute;top:0;left:0;width:711px;height:60px;z-index:3}
.brand{position:absolute;left:89px;top:22px;display:flex;align-items:center;gap:4px;font-weight:600;font-size:16px;color:var(--ink);letter-spacing:-.2px}
.brand-dot{width:14px;height:14px;border-radius:50%;background:var(--blue);margin-top:-14px}
.main-nav{position:absolute;right:89px;top:27px;display:flex;align-items:center;gap:26px}
.main-nav a{font-weight:600;font-size:7px;color:var(--ink);text-decoration:none}
.btn{display:inline-block;border-radius:10px;font-weight:700;font-size:7.5px;color:var(--white);padding:5px 8px;text-decoration:none;box-shadow:0 2px 2px rgba(0,0,0,.18);letter-spacing:.2px}
.btn-accent{background:var(--accent)}
.btn-blue{background:var(--blue)}

/* hero */
.hero-photo{position:absolute;left:0;top:0;width:711px;height:266px;clip-path:polygon(0 0,100% 0,100% 100%,0 90%);
  background:linear-gradient(90deg,#fff 0%,#f5f5f5 28%,rgba(230,232,234,1) 45%,#cfd3d6 62%,#b9a59a 78%,#8f8a88 100%)}
.hero-copy{position:absolute;left:89px;top:113px;z-index:2}
.hero-title{font-weight:700;font-size:17.5px;color:#111;letter-spacing:-.3px}
.hero-motto{font-weight:700;font-size:17.5px;color:var(--blue);letter-spacing:-.3px;margin-top:2px}
.hero-copy .btn{margin-top:10px}

/* section headings */
.section-head{position:absolute;left:89px;border-left:7px solid var(--accent);padding-left:6px;height:44px;display:flex;flex-direction:column;justify-content:center}
.section-head h2{font-size:13.5px;font-weight:600;color:var(--ink);line-height:1.35}
.section-head h2 span{display:block}

/* vision */
.vision-text{position:absolute;left:89px;width:533px;top:322px}
.vision-text p{margin-bottom:6px}
.values-label{position:absolute;left:89px;top:402px;font-weight:600;color:var(--ink)}
.values{position:absolute;left:89px;top:412px;width:533px;display:flex;justify-content:space-between}
.value{display:flex;align-items:center;gap:5px;font-size:7.5px}
.value svg{width:14px;height:14px;fill:var(--blue)}

/* mission */
.mission{position:absolute;left:0;top:494px;width:711px;height:182px;background:var(--mission)}
.mission-lead{position:absolute;left:89px;top:78px;font-size:7.5px;color:#1e2a30}
.mission-items{position:absolute;left:166px;top:100px;display:flex;gap:33px}
.mission-item{width:106px;text-align:center;color:#1e2a30;font-size:7.5px}
.mission-item svg{width:22px;height:24px;display:block;margin:0 auto 6px;fill:var(--white)}

/* team */
.team-lead{position:absolute;left:89px;top:755px;width:533px;font-size:7.5px}
.member-photo{position:absolute;width:89px;height:89px;border-radius:50%}
.member-name{position:absolute;text-align:center;font-size:7.5px;color:var(--ink)}
.member-name b{font-weight:700}
.member-bio{position:absolute;font-size:6.6px;line-height:1.6;color:var(--ink)}
.member-bio b{font-weight:700}

/* contact */
.contact{position:absolute;left:0;top:934px;width:711px;height:236px;clip-path:polygon(0 44px,100% 0,100% 100%,0 100%);
  background:linear-gradient(180deg,var(--contact-top) 0%,#6eb8de 45%,var(--contact-bottom) 100%)}
.contact-head{position:absolute;right:89px;top:977px;border-right:7px solid var(--accent);padding-right:6px;height:44px;text-align:right;display:flex;flex-direction:column;justify-content:center}
.contact-head h2{font-size:13.5px;font-weight:600;color:#203040;line-height:1.35}
.contact-head h2 span{display:block}
.field-label{position:absolute;font-size:7px;color:#1e2a30}
.field{position:absolute;background:var(--field);border:1px solid var(--field-line);font-size:7px;color:#b7bec3;padding:5px 6px}
.map{position:absolute;left:432px;top:1034px;width:190px;height:114px;background:linear-gradient(135deg,#bfe3b4 0%,#e9ece6 35%,#f1f0ec 65%,#a9d3ea 100%)}

.site-footer{position:absolute;left:0;top:1170px;width:711px;height:30px;background:var(--footer);color:var(--white);font-size:5.5px}
.site-footer .copy{position:absolute;left:89px;top:11px}
.social{position:absolute;right:89px;top:8px;display:flex;gap:4px}
.social span{width:11px;height:11px;border-radius:50%;background:var(--white)}
</style>
</head>
<body>

<header class="site-header">
  <div class="brand"><span>BrightKin</span><span class="brand-dot"></span></div>
  <nav class="main-nav">
    <a href="#vision">OUR VISION</a>
    <a href="#mission">OUR MISSION</a>
    <a href="#team">OUR TEAM</a>
    <a href="#partners">PARTNERS</a>
    <a href="#contact" class="btn btn-accent" style="color:#fff;font-size:7.5px">CONTACT US</a>
  </nav>
</header>

<div class="hero-photo" role="img" aria-label="Photo of a hand using a stylus on a tablet"></div>
<div class="hero-copy">
  <h1 class="hero-title">WE HELP PEOPLE HELP THEMSELVES</h1>
  <p class="hero-motto">DIRECT BRILLIANCE</p>
  <a href="#contact" class="btn btn-blue">CONTACT US</a>
</div>

<!-- Vision -->
<div class="section-head" id="vision" style="top:266px"><h2><span>OUR VISION</span><span>Who we are?</span></h2></div>
<div class="vision-text">
  <p>We are a direct response company that creates and sells information products and services that millions of people find interesting and important in their lives.</p>
  <p>We are specialized in the self-reliance market and we serve conservative Americans. We are in this business to serve globally and to grow individually. What we serve and inspire are people who need safety, comfort and peace of mind. We deliver empowerment through products that create fertile shortcuts to solutions, disentangle reality, simplify choices and ultimately make lives better. We give reassurance and confidence to these people through fresh, unique solutions.</p>
</div>
<div class="values-label">Values:</div>
<div class="values">
  <div class="value"><svg viewBox="0 0 16 16"><rect x="0" y="5" width="4" height="7"/><rect x="12" y="5" width="4" height="7"/><path d="M4 6h4l4 2v3l-3 1-5-1z"/></svg>Fairness</div>
  <div class="value"><svg viewBox="0 0 16 16"><path d="M8 9 4 5a2 2 0 0 1 4-2 2 2 0 0 1 4 2z"/><path d="M1 11h4l3 1 4-2 3 1-6 4H1z"/></svg>Caring</div>
  <div class="value"><svg viewBox="0 0 16 16"><path d="M8 1 14 3v5c0 4-3 6-6 7-3-1-6-3-6-7V3z"/><path d="M5 8l2 2 4-4" stroke="#fff" stroke-width="1.5" fill="none"/></svg>Safety</div>
  <div class="value"><svg viewBox="0 0 16 16"><path d="M1 4l6 3 7-5-3 8-5 4 1-5z"/></svg>Freedom</div>
  <div class="value"><svg viewBox="0 0 16 16"><circle cx="8" cy="3" r="2"/><path d="M5 6h6l-1 5H6z"/><path d="M1 10h3l4 3 4-3h3l-7 5z"/></svg>Unconditioned help</div>
</div>
<a href="#vision" class="btn btn-accent abs" style="left:89px;top:442px">READ MORE</a>

<!-- Mission -->
<section class="mission" id="mission">
  <div class="section-head" style="top:22px"><h2><span>OUR MISSION</span><span>What is it that we do?</span></h2></div>
  <p class="mission-lead">We are masters of direct response marketing. We create content and build solutions to profound challenges for millions of people.</p>
  <div class="mission-items">
    <div class="mission-item"><svg viewBox="0 0 22 24"><circle cx="11" cy="9" r="8"/><rect x="7" y="18" width="8" height="5" rx="1"/><circle cx="11" cy="9" r="3" fill="#8ec3da"/></svg>Create and aggregate great information product</div>
    <div class="mission-item"><svg viewBox="0 0 22 24"><path d="M4 2l5-1 7 15-3 3-3-2z"/><path d="M13 21c3 0 4-2 7-1" stroke="#fff" stroke-width="1.4" fill="none"/></svg>Write content that compels people to act</div>
    <div class="mission-item"><svg viewBox="0 0 22 24"><circle cx="15" cy="7" r="5" fill="none" stroke="#fff" stroke-width="2"/><path d="M11 11 3 14v8h12z"/></svg>Deep research to offer simple quick and easy solutions</div>
  </div>
</section>

<!-- Team -->
<div class="section-head" id="team" style="top:699px"><h2><span>OUR TEAM &amp; VALUES</span><span>Why are we the best?</span></h2></div>
<p class="team-lead">We're a small team of smart, funny hard-working specialists who are pushing to become the #1 company in self-reliance. High ambition, radical honesty and a result-oriented mindset are encouraged at BrightKin.</p>

<div class="member-photo" role="img" aria-label="Portrait photo of Dorin Vale" style="left:89px;top:792px;background:radial-gradient(circle at 50% 45%,#c9b4a4 0%,#9e8f86 45%,#e8ecef 100%)"></div>
<div class="member-name" style="left:74px;top:884px;width:120px"><b>Dorin Vale</b>,<br>CEO BrightKin</div>
<p class="member-bio" style="left:191px;top:790px;width:150px">Dorin started or was involved in 15 failed businesses before discovering online copywriting. After that, he ended up writing for Lumora Inc. and did 10-12 "successful" projects there, at least 3 of which broke the million-dollar mark. He wrote the famous HearthVolt, and the infamous CoilCraft and Harlow Motor sales letters. <b>Key personal strengths</b>: copywriting, consulting, positioning, idea generation, mentoring.</p>
<a href="#team" class="btn btn-accent abs" style="left:89px;top:920px">READ MORE</a>

<div class="member-photo" role="img" aria-label="Portrait photo of Marco Vale" style="left:368px;top:793px;background:radial-gradient(circle at 50% 45%,#c7a08c 0%,#5a4a44 45%,#1c1c1f 100%)"></div>
<div class="member-name" style="left:352px;top:888px;width:120px"><b>Marco Vale</b>,<br>Cofounder &amp; Affiliate<br>Manager BrightKin</div>
<p class="member-bio" style="left:470px;top:790px;width:152px">Since the company's late 2012 start, Marco grew a network of 5000 affiliates, that dominates TradeHub's survival niche - 3 out of top 5 products are BrightKin offers, under the Prepwise brand. <b>Key personal strengths</b>: strong networking skills, sales, risk management, leadership.</p>
<a href="#team" class="btn btn-accent abs" style="left:556px;top:903px">READ MORE</a>

<!-- Contact -->
<section class="contact" id="contact"></section>
<div class="contact-head"><h2><span>CONTACT US</span><span>Wana talk?</span></h2></div>

<div class="field-label" style="left:89px;top:1022px">*Name:</div>
<div class="field" style="left:89px;top:1034px;width:134px;height:19px">Write full name</div>
<div class="field-label" style="left:89px;top:1056px">*Email:</div>
<div class="field" style="left:89px;top:1068px;width:134px;height:19px">Write email adress</div>
<div class="field-label" style="left:89px;top:1090px">Website:</div>
<div class="field" style="left:89px;top:1102px;width:134px;height:19px">Write website adress</div>
<div class="field-label" style="left:236px;top:1022px">Message:</div>
<div class="field" style="left:236px;top:1034px;width:180px;height:88px">Write your message</div>
<a href="#contact" class="btn btn-accent abs" style="left:330px;top:1129px;padding:5px 10px">SEND MESSAGE</a>
<div class="map" role="img" aria-label="Street map showing the office location"></div>

<footer class="site-footer">
  <span class="copy">Copyright @ 2018 BrightKin. All rights reserved.</span>
  <div class="social"><span></span><span></span><span></span></div>
</footer>

</body>
</html>
```